Skin rejuvenation webpage

I already have functioning websites, novawell.care and kindredclinicfirst.com. I need to create a page to add that captures the general overarching theme of these two websites, while educating and advertising our new offering of skin rejuvenation in our clinic. 9 Vita and Harbor Care Clinic are both one clinic. 9 Vita is a membership model healthcare clinic and Harbor Care Clinic is a regular traditional medical clinic that uses health insurance. The skin rejuvenation is CASH PAY only, so no insurance is billed. We give large discounts to those who are current members of 9 Vita.

For title, something like, "“Smooth wrinkles. Restore skin. Age intelligently." And subtitle something like "Lumeza + Advanced Laser (ClariVo) for complete skin rejuvenation".

Lumeza → relaxes muscles Laser → improves skin quality
Combine them = better results
Step 1: Lumeza Smooth dynamic wrinklesPrevent deeper lines
Step 2: ClariVo Laser Reduce redness, pigmentation Improve collagen + texture

Or Bold headline ("CLARIVo Laser | The New Gold Standard"), subhead emphasizing "no downtime, no numbing, treats over 25 indications including fine lines and wrinkles," with immediate phone/CTA buttons.

Layout: Clean sections—overview of how it works (wavelength explanations: yellow for vascular/redness, infrared for collagen), benefits bullets, detailed before/after photo galleries (e.g., "Before and After 1 Treatment for Skin Rejuvenation" showing smoother, firmer skin).

Before/after photos: https://brivotherm.com/results/
“Start with a personalized skin plan”

Book now
Limited appointments (scarcity)

```html
<!DOCTYPE html>
<html lang="en">
<head>
<meta charset="utf-8">
<title>Skin Rejuvenation – 9 Vita</title>
<link rel="stylesheet" href="https://fonts.googleapis.com/css2?family=Poppins:ital,wght@0,400;0,500;0,600;0,700;0,800;1,400&display=swap">
<style>
:root{
  --orange:#f59a3c;
  --blue:#1a8cbf;
  --blue-dark:#1479a8;
  --ink:#2b2b2b;
  --text:#444;
  --muted:#666;
  --gray-bg:#efefef;
  --footer:#272727;
  --white:#fff;
  --footer-text:#e8e8e8;
}
*{box-sizing:border-box;margin:0;padding:0}
html,body{width:1200px;height:5199px;overflow:hidden}
body{position:relative;font-family:"Poppins",sans-serif;color:var(--text);background:var(--white)}
.abs{position:absolute}
.photo{position:absolute;border-radius:10px;overflow:hidden}

/* header */
.site-header{position:absolute;left:0;top:0;width:1200px;height:82px;background:#fff;border-bottom:1px solid #e4e4e4}
.brand{position:absolute;display:flex;align-items:center;gap:8px;font-weight:700;color:var(--blue);font-size:22px}
.brand .dot{width:26px;height:26px;border-radius:50%;background:var(--orange)}
.main-nav{position:absolute;left:295px;top:31px;display:flex;font-size:14px;color:#333}
.main-nav a{text-decoration:none;color:#333;margin-right:30px}
.main-nav a.active{color:var(--blue);font-weight:600}
.btn{display:inline-flex;align-items:center;justify-content:center;background:var(--orange);color:#fff;font-weight:700;text-transform:uppercase;border-radius:40px;text-decoration:none;letter-spacing:.3px}

/* hero */
.hero{position:absolute;left:0;top:82px;width:1200px;height:638px;overflow:hidden}
.hero-bg{position:absolute;inset:0;background:linear-gradient(100deg,#3f7f86 0%,#4c8a90 45%,#6f9ea2 70%,#8fb3b4 100%)}
.hero h1{position:absolute;left:75px;top:105px;font-size:46px;line-height:52px;font-weight:800;color:#fff;text-transform:uppercase;letter-spacing:.5px}
.hero p{position:absolute;left:75px;top:268px;width:625px;font-size:18px;line-height:29.5px;font-weight:600;color:#fff}
.hero .btn{position:absolute;left:75px;top:430px;width:166px;height:64px;font-size:15px}
.hero .scarcity{position:absolute;left:75px;top:502px;font-size:14px;font-style:italic;color:#fff;text-decoration:underline}
.dots{position:absolute;left:75px;top:575px;display:flex;gap:10px}
.dots span{width:8px;height:8px;border-radius:50%;background:rgba(255,255,255,.6)}
.dots span.on{background:#fff}

/* how it works */
.how-bg{position:absolute;left:0;top:850px;width:1200px;height:1006px;background:var(--gray-bg)}
.section-title{position:absolute;font-size:38px;font-weight:700;color:var(--ink)}
.step-card{position:absolute;background:#fff;border-radius:10px;padding:22px 22px 18px 22px;box-shadow:0 1px 3px rgba(0,0,0,.05)}
.step-card h3{font-size:16px;font-weight:700;color:var(--blue);line-height:22px;margin-bottom:12px}
.step-card p{font-size:12.5px;line-height:20px;color:#444}
.arrow-badge{position:absolute;width:60px;height:60px;border-radius:50%;background:var(--orange);display:flex;align-items:center;justify-content:center}

/* treatment */
.treat-text{position:absolute;left:603px;top:2017px;width:525px}
.treat-text h3{font-size:20px;font-weight:700;color:var(--blue);margin-bottom:12px}
.treat-text p{font-size:14px;line-height:24px;color:#444;margin-bottom:22px}
.ticks{list-style:none}
.ticks li{display:flex;align-items:center;gap:14px;font-size:14px;color:#444;height:38px}

/* benefits */
.benefits{position:absolute;left:0;top:2376px;width:1200px;height:454px;background:var(--blue);overflow:hidden}
.benefits h2{position:absolute;left:75px;top:95px;font-size:40px;font-weight:700;color:#fff}
.benefit-list{position:absolute;left:75px;top:163px;list-style:none}
.benefit-list li{display:flex;align-items:center;gap:12px;height:40px;font-size:17px;color:#fff}
.benefit-list .chk{width:18px;height:18px;border-radius:50%;background:var(--orange);display:flex;align-items:center;justify-content:center}

/* gallery */
.compare{position:absolute;border-radius:10px;overflow:hidden}
.compare .half{position:absolute;top:0;bottom:0}
.compare .divider{position:absolute;top:0;bottom:0;width:4px;background:#fff}
.compare .handle{position:absolute;border-radius:50%;background:#fff;display:flex;align-items:center;justify-content:center}
.compare .lbl{position:absolute;font-weight:700;color:#fff}
.caption{position:absolute;left:0;width:1200px;text-align:center;font-size:18px;color:#333}

/* cta */
.cta{position:absolute;left:392px;top:4504px;width:416px;height:62px;font-size:15px}

/* footer */
.site-footer{position:absolute;left:0;top:4670px;width:1200px;height:529px;background:var(--footer)}
.promo{position:absolute;left:90px;top:4629px;width:1020px;height:82px;background:var(--blue);border-radius:41px;z-index:2}
.promo h2{position:absolute;left:44px;top:20px;font-size:32px;font-weight:700;color:#fff}
.promo .btn{position:absolute;right:10px;top:10px;width:162px;height:62px;font-size:15px}
.f-col{position:absolute;top:4790px;color:#fff}
.f-col h4{font-size:21px;font-weight:700;margin-bottom:10px;color:#fff}
.f-col a,.f-col li{display:block;color:var(--footer-text);font-size:13.5px;line-height:32px;text-decoration:none;list-style:none}
.f-about{position:absolute;left:75px;top:4868px;width:245px;font-size:14px;line-height:26px;color:var(--footer-text)}
.hours li{line-height:18px;margin-bottom:18px;font-size:14px;color:var(--footer-text)}
.hours em{display:block;font-size:12px;color:#cfcfcf}
.hours li.closed{color:var(--orange)}
.socials{display:flex;gap:18px;margin-top:18px}
.socials span{width:18px;height:18px;border-radius:50%;background:#bfbfbf}
.socials span.x{background:var(--orange)}
.copyright{position:absolute;left:0;top:5142px;width:1200px;text-align:center;font-size:12px;color:#cfcfcf}
</style>
</head>
<body>

<header class="site-header">
  <div class="brand" style="left:75px;top:24px"><span class="dot"></span>9 Vita</div>
  <nav class="main-nav">
    <a class="active" href="#">Home</a>
    <a href="#">Our Providers</a>
    <a href="#">Services</a>
    <a href="#">9 Vita</a>
    <a href="#">Blog</a>
    <a href="#">Patient Forms</a>
    <a href="#">Contact</a>
  </nav>
  <a class="btn" href="#" style="position:absolute;left:962px;top:10px;width:164px;height:62px;font-size:15px">Book Now</a>
</header>

<section class="hero">
  <div class="hero-bg" role="img" aria-label="Photo of a woman receiving a laser skin treatment"></div>
  <h1>Smooth wrinkles.<br>Restore skin.<br>Age intelligently.</h1>
  <p>Discover ClariVo, an advanced device that uses two different wavelengths (589nm and 1319 nm) to treat a multitude of different skin conditions including acne, rosacea, vascular issues, scars, melasma, pigment and skin rejuvenation, consistently delivering long-lasting results.</p>
  <a class="btn" href="#">Book Now</a>
  <span class="scarcity">Limited appointments</span>
  <div class="dots"><span class="on"></span><span></span><span></span><span></span></div>
</section>

<!-- How it works -->
<div class="how-bg"></div>
<h2 class="section-title" style="left:72px;top:940px">How it Works</h2>

<div class="photo" style="left:615px;top:790px;width:511px;height:364px;background:linear-gradient(135deg,#e9b48f,#c98962 60%,#8c5a3e)" role="img" aria-label="Microneedling pen on a treated cheek"></div>

<div class="step-card" style="left:75px;top:1018px;width:510px;height:172px">
  <h3>589nm for acne, rosacea and pigmented lesions</h3>
  <p>The 589nm wavelength, with a penetration depth of up to 1.25mm, is preferentially absorbed by oxyhemoglobin and targets c.acne bacteria and pigmented lesions. This makes it the gold standard for treating acne, rosacea, vascular concerns, pigmented lesions and melasma.</p>
</div>

<div class="arrow-badge" style="left:574px;top:1153px">
  <svg width="26" height="26" viewBox="0 0 26 26" fill="none" stroke="#fff" stroke-width="3" stroke-linecap="round" stroke-linejoin="round"><path d="M5 5 L21 21 M21 9 V21 H9"/></svg>
</div>

<div class="photo" style="left:75px;top:1214px;width:510px;height:363px;background:linear-gradient(135deg,#a7b2bf,#d7b6a2 55%,#7c6a66)" role="img" aria-label="Woman with protective glasses receiving a light therapy treatment"></div>

<div class="step-card" style="left:615px;top:1190px;width:511px;height:167px">
  <h3>1319 for collagen stimulation around fine lines and wrinkles</h3>
  <p>The 1319nm wavelength penetrates up to 2mm and is preferentially absorbed by water making it safer for darker skin types. It stimulates fibroblasts and promotes collagen production for non-ablative skin resurfacing, while also providing a thermal impact to sebaceous glands to regulate oil and sebum production.</p>
</div>

<div class="photo" style="left:615px;top:1390px;width:511px;height:362px;background:linear-gradient(135deg,#e7e7ea,#d6b9a6 50%,#3f63b5)" role="img" aria-label="Injection being given to a woman's forehead by a gloved practitioner"></div>

<div class="step-card" style="left:75px;top:1605px;width:510px;height:172px">
  <h3>Botulinum toxin injections for deeper wrinkles</h3>
  <p>Repeated facial muscle retractions over many years create deeper, longer lasting skin furrows that add years to facial expressions. Botulinum toxin injections temporarily paralyze muscles that cause frown lines, crow's feet, and forehead lines.</p>
</div>

<div class="arrow-badge" style="left:550px;top:1583px">
  <svg width="26" height="26" viewBox="0 0 26 26" fill="none" stroke="#fff" stroke-width="3" stroke-linecap="round" stroke-linejoin="round"><path d="M21 5 L5 21 M5 9 V21 H17"/></svg>
</div>

<!-- Treatments -->
<h2 class="section-title" style="left:0;width:1200px;text-align:center;top:1920px">Treatments One Complete Result</h2>
<div class="photo" style="left:75px;top:2011px;width:503px;height:280px;background:linear-gradient(120deg,#e7e3df,#d8b7a3 45%,#f2f2f2)" role="img" aria-label="Woman with eye shields receiving a handheld laser facial"></div>
<div class="treat-text">
  <h3>CLARIVo Laser</h3>
  <p>The CLARIVo uses two precise wavelengths to target &nbsp;redness, pigmentation, and stimulate collagen deep within the dermis — with no downtime and no numbing cream required.</p>
  <ul class="ticks">
    <li><svg width="14" height="12" viewBox="0 0 14 12"><path d="M1.5 6.5 L5 10 L12.5 1.5" fill="none" stroke="#1a8cbf" stroke-width="2.6" stroke-linecap="round" stroke-linejoin="round"/></svg>Reduce redness &amp; rosacea</li>
    <li><svg width="14" height="12" viewBox="0 0 14 12"><path d="M1.5 6.5 L5 10 L12.5 1.5" fill="none" stroke="#1a8cbf" stroke-width="2.6" stroke-linecap="round" stroke-linejoin="round"/></svg>Fade pigmentation &amp; sunspots</li>
    <li><svg width="14" height="12" viewBox="0 0 14 12"><path d="M1.5 6.5 L5 10 L12.5 1.5" fill="none" stroke="#1a8cbf" stroke-width="2.6" stroke-linecap="round" stroke-linejoin="round"/></svg>Stimulate Type I &amp; III collagen</li>
    <li><svg width="14" height="12" viewBox="0 0 14 12"><path d="M1.5 6.5 L5 10 L12.5 1.5" fill="none" stroke="#1a8cbf" stroke-width="2.6" stroke-linecap="round" stroke-linejoin="round"/></svg>Improve texture, tone &amp; firmness</li>
  </ul>
</div>

<!-- Benefits -->
<section class="benefits">
  <svg class="abs" style="left:0;top:0" width="1200" height="454" viewBox="0 0 1200 454" role="img" aria-label="Practitioner performing a laser treatment on a reclining patient">
    <defs><linearGradient id="clinic" x1="0" y1="0" x2="1" y2="1"><stop offset="0" stop-color="#bcd9e4"/><stop offset=".5" stop-color="#8fc2d6"/><stop offset="1" stop-color="#5d8fa6"/></linearGradient></defs>
    <polygon points="592,0 1200,0 1200,454 445,454" fill="url(#clinic)"/>
  </svg>
  <h2>Benefits</h2>
  <ul class="benefit-list">
    <li><span class="chk"><svg width="10" height="8" viewBox="0 0 10 8"><path d="M1 4 L4 7 L9 1" fill="none" stroke="#fff" stroke-width="2"/></svg></span>No anesthesia</li>
    <li><span class="chk"><svg width="10" height="8" viewBox="0 0 10 8"><path d="M1 4 L4 7 L9 1" fill="none" stroke="#fff" stroke-width="2"/></svg></span>Minimal discomfort</li>
    <li><span class="chk"><svg width="10" height="8" viewBox="0 0 10 8"><path d="M1 4 L4 7 L9 1" fill="none" stroke="#fff" stroke-width="2"/></svg></span>Skin types I-IV</li>
    <li><span class="chk"><svg width="10" height="8" viewBox="0 0 10 8"><path d="M1 4 L4 7 L9 1" fill="none" stroke="#fff" stroke-width="2"/></svg></span>Non invasive</li>
    <li><span class="chk"><svg width="10" height="8" viewBox="0 0 10 8"><path d="M1 4 L4 7 L9 1" fill="none" stroke="#fff" stroke-width="2"/></svg></span>Year-round treatments</li>
  </ul>
</section>

<!-- Before & After -->
<h2 class="section-title" style="left:0;width:1200px;text-align:center;top:2868px">Before &amp; After Galleries</h2>

<div class="compare" style="left:75px;top:2959px;width:1051px;height:464px">
  <div class="half" style="left:0;width:525px;background:linear-gradient(90deg,#2e3338,#a98672 60%,#c8a08a)" role="img" aria-label="Before: close-up of a woman's eye area with visible wrinkles"></div>
  <div class="half" style="left:525px;width:526px;background:linear-gradient(90deg,#d3ad96,#b58d78 45%,#2e3338)" role="img" aria-label="After: the same eye area with smoother skin"></div>
  <div class="divider" style="left:523px"></div>
  <div class="handle" style="left:500px;top:208px;width:48px;height:48px">
    <svg width="24" height="14" viewBox="0 0 24 14" fill="none" stroke="#333" stroke-width="2" stroke-linecap="round" stroke-linejoin="round"><path d="M7 1 L1 7 L7 13 M17 1 L23 7 L17 13"/></svg>
  </div>
  <span class="lbl" style="left:20px;bottom:24px;font-size:18px">Before</span>
  <span class="lbl" style="right:38px;bottom:24px;font-size:18px">After</span>
</div>
<p class="caption" style="top:3448px">Treatment for Skin Rejuvenation</p>

<div class="compare" style="left:75px;top:3520px;width:512px;height:292px">
  <div class="half" style="left:0;width:255px;background:linear-gradient(135deg,#c97a66,#e0a08a)" role="img" aria-label="Before: cheek with redness"></div>
  <div class="half" style="left:255px;width:257px;background:linear-gradient(135deg,#e7b6a0,#d69a84)" role="img" aria-label="After: calmer, even cheek"></div>
  <div class="divider" style="left:253px"></div>
  <div class="handle" style="left:232px;top:123px;width:46px;height:46px"><svg width="22" height="14" viewBox="0 0 24 14" fill="none" stroke="#333" stroke-width="2" stroke-linecap="round" stroke-linejoin="round"><path d="M7 1 L1 7 L7 13 M17 1 L23 7 L17 13"/></svg></div>
  <span class="lbl" style="left:20px;bottom:22px;font-size:15px">Before</span><span class="lbl" style="right:22px;bottom:22px;font-size:15px">After</span>
</div>
<div class="compare" style="left:615px;top:3520px;width:511px;height:292px">
  <div class="half" style="left:0;width:255px;background:linear-gradient(135deg,#b8805f,#d5a27f)" role="img" aria-label="Before: skin with sun spots"></div>
  <div class="half" style="left:255px;width:256px;background:linear-gradient(135deg,#e8c4a6,#ddb292)" role="img" aria-label="After: clearer, brighter skin"></div>
  <div class="divider" style="left:253px"></div>
  <div class="handle" style="left:232px;top:123px;width:46px;height:46px"><svg width="22" height="14" viewBox="0 0 24 14" fill="none" stroke="#333" stroke-width="2" stroke-linecap="round" stroke-linejoin="round"><path d="M7 1 L1 7 L7 13 M17 1 L23 7 L17 13"/></svg></div>
  <span class="lbl" style="left:20px;bottom:22px;font-size:15px">Before</span><span class="lbl" style="right:22px;bottom:22px;font-size:15px">After</span>
</div>

<div class="compare" style="left:75px;top:3836px;width:512px;height:295px">
  <div class="half" style="left:0;width:255px;background:linear-gradient(135deg,#8e6a5a,#c98f7c)" role="img" aria-label="Before: cheek with active acne"></div>
  <div class="half" style="left:255px;width:257px;background:linear-gradient(135deg,#c9c6c4,#d5a592)" role="img" aria-label="After: cheek with reduced acne"></div>
  <div class="divider" style="left:253px"></div>
  <div class="handle" style="left:232px;top:124px;width:46px;height:46px"><svg width="22" height="14" viewBox="0 0 24 14" fill="none" stroke="#333" stroke-width="2" stroke-linecap="round" stroke-linejoin="round"><path d="M7 1 L1 7 L7 13 M17 1 L23 7 L17 13"/></svg></div>
  <span class="lbl" style="left:20px;bottom:22px;font-size:15px">Before</span><span class="lbl" style="right:22px;bottom:22px;font-size:15px">After</span>
</div>
<div class="compare" style="left:615px;top:3836px;width:511px;height:295px">
  <div class="half" style="left:0;width:255px;background:linear-gradient(135deg,#4a3a36,#a86f5f)" role="img" aria-label="Before: face with acne scarring"></div>
  <div class="half" style="left:255px;width:256px;background:linear-gradient(135deg,#3a302e,#c2937e)" role="img" aria-label="After: smoother, clearer complexion"></div>
  <div class="divider" style="left:253px"></div>
  <div class="handle" style="left:232px;top:124px;width:46px;height:46px"><svg width="22" height="14" viewBox="0 0 24 14" fill="none" stroke="#333" stroke-width="2" stroke-linecap="round" stroke-linejoin="round"><path d="M7 1 L1 7 L7 13 M17 1 L23 7 L17 13"/></svg></div>
  <span class="lbl" style="left:20px;bottom:22px;font-size:15px">Before</span><span class="lbl" style="right:22px;bottom:22px;font-size:15px">After</span>
</div>

<div class="compare" style="left:75px;top:4157px;width:512px;height:293px">
  <div class="half" style="left:0;width:255px;background:linear-gradient(135deg,#7a5a4c,#c48a72)" role="img" aria-label="Before: man's face with redness"></div>
  <div class="half" style="left:255px;width:257px;background:linear-gradient(135deg,#5f4a42,#d2a08a)" role="img" aria-label="After: man's face with even tone"></div>
  <div class="divider" style="left:253px"></div>
  <div class="handle" style="left:232px;top:123px;width:46px;height:46px"><svg width="22" height="14" viewBox="0 0 24 14" fill="none" stroke="#333" stroke-width="2" stroke-linecap="round" stroke-linejoin="round"><path d="M7 1 L1 7 L7 13 M17 1 L23 7 L17 13"/></svg></div>
  <span class="lbl" style="left:20px;bottom:22px;font-size:15px">Before</span><span class="lbl" style="right:22px;bottom:22px;font-size:15px">After</span>
</div>
<div class="compare" style="left:615px;top:4157px;width:511px;height:293px">
  <div class="half" style="left:0;width:255px;background:linear-gradient(135deg,#6e5246,#c6977c)" role="img" aria-label="Before: woman's face with pigmentation"></div>
  <div class="half" style="left:255px;width:256px;background:linear-gradient(135deg,#d9b39b,#8e6a58)" role="img" aria-label="After: woman's face with lighter pigmentation"></div>
  <div class="divider" style="left:253px"></div>
  <div class="handle" style="left:232px;top:123px;width:46px;height:46px"><svg width="22" height="14" viewBox="0 0 24 14" fill="none" stroke="#333" stroke-width="2" stroke-linecap="round" stroke-linejoin="round"><path d="M7 1 L1 7 L7 13 M17 1 L23 7 L17 13"/></svg></div>
  <span class="lbl" style="left:20px;bottom:22px;font-size:15px">Before</span><span class="lbl" style="right:22px;bottom:22px;font-size:15px">After</span>
</div>

<a class="btn cta" href="#">Start with a personalized skin plan</a>

<!-- Footer -->
<footer class="site-footer"></footer>
<div class="promo">
  <h2>50% Discount for all 9 Vita Members</h2>
  <a class="btn" href="#">Book Now</a>
</div>

<div class="brand" style="left:75px;top:4800px"><span class="dot"></span>9 Vita</div>
<p class="f-about">Duis aute irure dolor in reprehenderit in voluptate velit esse cillum dolore eu fugiat nulla pariatu</p>

<div class="f-col" style="left:385px">
  <h4>Quick Links</h4>
  <a href="#">Home</a><a href="#">Our Providers</a><a href="#">Services</a><a href="#">9 Vita</a><a href="#">Blog</a><a href="#">Patient Forms</a><a href="#">Contact</a>
</div>

<div class="f-col" style="left:611px;width:260px">
  <h4>Contact Info</h4>
  <p style="font-size:13.5px;line-height:24px;color:var(--footer-text);margin-bottom:14px">4820 Meadowlark Lane, Suite 210<br>Lakeview, TX 75099</p>
  <a href="#">(555) 014-2870</a>
  <a href="#">info@ninevita.care</a>
  <div class="socials"><span></span><span class="x"></span><span></span><span></span><span></span></div>
</div>

<div class="f-col" style="left:903px;width:240px">
  <h4>Contact Info</h4>
  <ul class="hours">
    <li>Monday: 8 am - 5 pm,<em>Closed 1-2 pm for lunch</em></li>
    <li>Tuesday: 8 am - 6 pm,<em>Closed 1-2 pm for lunch</em></li>
    <li>Wednesday: 8 am - 5 pm,<em>Closed 1-2 pm for lunch</em></li>
    <li>Thursday: 8 am - 6 pm,<em>Closed 1-2 pm for lunch</em></li>
    <li>Friday: 8 am - 5 pm,<em>Closed 1-2 pm for lunch</em></li>
    <li class="closed">Closed Saturday &amp; Sunday</li>
  </ul>
</div>

<p class="copyright">Copyright © 2026 Company Name All rights reserved</p>

</body>
</html>
```